Lumaform website scandinavian interior design

Existing website: http://lumaform-example.no/

Webdesign for interior designer Ragna Tvedtholm. The company name is Lumaform. Scandinavian interiør is known to be simple and elegant. The website will be in Norwegian, we are working on the text. The website needs to have a few more pages than just the front page. Here are the different titles of the pages:

1. Hjem
2. Om Lumaform
3. Tjenester og priser
4.. Kontakt oss

There should be Facebook and Instagram icons somewhere at the bottom of the website.

The logo we want to use is attached (pink with black print, see attachment )

We have attached images for inspiration. We want to use some of these colors. The color in the logo, The style should be elegant, modern and delicate.

It is imprtant that the website is user friendly.

Target Market(s)

People who want to decorate their home
Companies and public sector who need to redecorate

Industry/Entity Type

Interior Designer

Coding

Coded - Design and coding required

Number of Pages Required

5+ page

Font styles to use
Other font styles liked:
• see example in the logo breakdown

Requirements
Must have
• Elegant, modern and delicate design
Images of design, see examples attached
Colors similar to the pictures
Should not have
• Too bright colors
Pictures of people

```html
<!DOCTYPE html>
<html lang="no">
<head>
<meta charset="utf-8">
<title>Lumaform – Farge &amp; interiørdesign</title>
<link href="https://fonts.googleapis.com/css2?family=Poppins:wght@300;400;500;600;700;800&family=Cormorant+Garamond:ital,wght@0,400;1,400&display=swap" rel="stylesheet">
<style>
:root{
  --ink:#3d3d3d;
  --ink-soft:#555;
  --muted:#9a9a9a;
  --hero-wall:#ecebe7;
  --mint:#cfe3dc;
  --card:#f8f8f8;
  --band:#f9f9f9;
  --line:#e3e3e8;
  --icon-grey:#b7bac6;
  --icon-stroke:#8d90a8;
  --accent-blue:#3550d2;
  --footer:#c0b8b8;
  --footer-field:#cec7c7;
  --footer-button:#adb3cb;
  --white:#ffffff;
}
*{box-sizing:border-box;margin:0;padding:0}
html,body{width:1200px;height:4132px;overflow:hidden;background:var(--white)}
body{position:relative;font-family:'Poppins',sans-serif;color:var(--ink)}
.abs{position:absolute}
.photo{position:absolute}

/* header */
.brand{left:209px;top:28px;font-family:'Cormorant Garamond',serif;font-style:italic;font-size:40px;color:var(--ink);display:flex;align-items:center;gap:10px}
.brand-dot{width:10px;height:10px;border-radius:50%;background:#e7c8c8}
.nav{left:670px;top:15px;display:flex;gap:22px;font-size:9px;color:var(--ink-soft)}
.nav a{color:inherit;text-decoration:none}
.nav .active{color:#b0b0b0}

/* hero */
.hero-photo{left:441px;top:43px;width:526px;height:636px;background:linear-gradient(160deg,#f0efec,#e6e4df)}
.hero-title{left:217px;top:218px;font-size:38px;font-weight:800;line-height:53px;color:#474747;letter-spacing:-.8px}
.hero-text{left:217px;top:392px;width:370px;font-size:10.5px;line-height:16.5px;color:var(--ink-soft)}
.btn-works{left:217px;top:460px;width:100px;height:33px;border-radius:17px;background:var(--mint);font-size:9.5px;display:flex;align-items:center;justify-content:center;color:var(--ink)}
.since{left:978px;top:322px;writing-mode:vertical-rl;font-size:8px;letter-spacing:3px;color:var(--ink-soft)}
.hero-dots{left:592px;top:648px;display:flex;gap:6px}
.hero-dots i{width:4px;height:4px;border-radius:50%;background:#d8d6d0}
.hero-dots i:first-child{background:#fff}

/* about */
.about-photo{left:225px;top:746px;width:312px;height:479px;background:linear-gradient(180deg,#eceef0 0%,#f6f6f6 55%,#b9c1c6 80%,#d9dde0 100%)}
.eyebrow{font-size:7.5px;font-weight:600;letter-spacing:1.5px;color:var(--ink)}
.about-eyebrow{left:622px;top:750px}
.about-title{left:622px;top:766px;font-size:16.5px;font-weight:500;line-height:25px;width:330px}
.about-body{left:594px;top:845px;width:376px;font-size:9px;line-height:17px;color:var(--ink-soft)}
.about-body p+p{margin-top:12px}
.learn{left:594px;top:1152px;font-size:9.5px;color:var(--ink);border-bottom:1px solid var(--ink);padding-bottom:1px}

/* section heads */
.sec-title{font-size:16.5px;font-weight:500;color:var(--ink)}
.sec-lead{left:513px;width:460px;font-size:9px;line-height:17px;color:var(--muted)}

/* workflow */
.flow-step{position:absolute;top:1375px;width:240px}
.flow-circle{width:58px;height:58px;border-radius:50%;background:var(--icon-grey);display:flex;align-items:center;justify-content:center}
.flow-line{position:absolute;top:28px;left:68px;width:166px;height:1px;background:var(--line)}
.flow-line::after{content:"";position:absolute;right:-2px;top:-2px;width:5px;height:5px;border-radius:50%;background:var(--line)}
.step-title{margin:16px 0 0 5px;font-size:10px;font-weight:600;letter-spacing:.3px}
.step-text{margin:6px 0 0 5px;width:215px;font-size:9px;line-height:17px;color:var(--muted)}

/* services */
.service-card{position:absolute;width:238px;height:157px;background:var(--card);padding:16px 18px}
.service-card h3{margin-top:13px;font-size:10px;font-weight:600;letter-spacing:.3px}
.service-card p{margin-top:7px;font-size:9px;line-height:17px;color:var(--muted);width:205px}

/* projects */
.filters{left:513px;top:2173px;display:flex;gap:9px;font-size:7px;font-weight:500;letter-spacing:.8px;color:var(--ink-soft)}
.filters b{font-weight:700;color:var(--ink)}
.tile{position:absolute;width:300px;height:299px}
.tile-feature{background:var(--accent-blue);color:#fff;padding:14px 19px}
.tile-feature .kicker{font-size:7.5px;letter-spacing:1px;opacity:.75}
.tile-feature h4{margin-top:4px;font-size:17px;font-weight:400}
.expand{position:absolute;left:19px;bottom:13px;width:28px;height:28px;border:1px solid rgba(255,255,255,.8);border-radius:50%}

/* blog */
.blog-band{left:0;top:2828px;width:1200px;height:661px;background:var(--band)}
.post{position:absolute;top:3157px;width:238px}
.post .photo{position:relative;width:238px;height:162px}
.post h4{margin:22px 0 0 9px;font-size:12.5px;font-weight:500;line-height:18px;width:175px}

/* clients */
.client{position:absolute;top:3652px;width:135px;height:73px;border:1px solid #ececec;display:flex;align-items:center;justify-content:center;font-size:8.5px;font-weight:700;letter-spacing:-.2px}
.client-dots{left:560px;top:3755px;display:flex;gap:6px}
.client-dots i{width:6px;height:6px;border-radius:50%;background:#d9d9d9}
.client-dots i:first-child{background:#9b9b9b}

/* footer */
.footer{left:0;top:3830px;width:1200px;height:302px;background:var(--footer);color:var(--white)}
.f-col{position:absolute;top:53px;width:240px}
.f-col h5{font-size:11px;font-weight:400}
.f-col p{margin-top:20px;font-size:8px;line-height:15px;opacity:.85}
.f-list{margin-top:20px;list-style:none;font-size:8px;line-height:15px;opacity:.9}
.f-list li::before{content:"→ ";}
.socials{margin-top:20px;display:flex;gap:14px}
.social-dot{width:18px;height:18px;border-radius:50%;background:rgba(255,255,255,.25)}
.field{margin-top:23px;height:28px;background:var(--footer-field);display:flex;align-items:center;justify-content:center;font-size:8.5px}
.subscribe{margin-top:8px;height:28px;background:var(--footer-button);display:flex;align-items:center;justify-content:center;font-size:8.5px}
.copy{position:absolute;left:0;width:1200px;top:240px;text-align:center;font-size:8px;opacity:.85}
</style>
</head>
<body>

<header>
  <div class="abs brand"><span>Lumaform</span><span class="brand-dot"></span></div>
  <nav class="abs nav">
    <a class="active">Hjem</a><a>Om Lumaform</a><a>Tjenester og priser</a><a>Blog</a><a>Kontakt</a>
  </nav>
</header>

<section class="hero">
  <div class="photo hero-photo" role="img" aria-label="Wooden wall crate with trailing green ivy against a pale wall"></div>
  <h1 class="abs hero-title">We Create Amazing<br>Architecture<br>Designs</h1>
  <p class="abs hero-text">A small river named Duden flows by their place and supplies it with the necessary regelialia. It is a paradisematic country, in which roasted parts of sentences fly into your mouth.</p>
  <a class="abs btn-works">View our works</a>
  <div class="abs since">SINCE - 2018</div>
  <div class="abs hero-dots"><i></i><i></i><i></i></div>
</section>

<section class="about">
  <div class="photo about-photo" role="img" aria-label="Bright white kitchen with pendant light and grey island"></div>
  <div class="abs eyebrow about-eyebrow">ABOUT</div>
  <h2 class="abs about-title">We are the best Interior, Exterior &amp; Architecture Firm</h2>
  <div class="abs about-body">
    <p>Lorem ipsum dolor sit amet, consectetur adipiscing elit. Nullam vestibulum urna mollis, tristique odio id, scelerisque elit. Suspendisse quis mattis magna. Aenean sed pharetra ante, non pulvinar arcu. Nunc massa turpis, volutpat eget euismod a, maximus non justo. Nunc et velit eget sapien vulputate aliquet. Quisque sollicitudin auctor libero, eu feugiat tellus blandit ut. Curabitur iaculis imperdiet mauris. Lorem ipsum dolor sit amet, consectetur adipiscing elit. Nullam vestibulum urna mollis, tristique odio id, scelerisque elit. Suspendisse quis mattis magna. Aenean sed pharetra ante, non pulvinar arcu. Nunc massa turpis, volutpat eget euismod a, maximus non justo. Nunc et velit eget sapien vulputate aliquet. Quisque sollicitudin auctor libero, eu feugiat tellus blandit ut. Curabitur iaculis imperdiet mauris.</p>
    <p>Lorem ipsum dolor sit amet, consectetur adipiscing elit. Nullam vestibulum urna mollis, tristique odio id, scelerisque elit. Suspendisse quis mattis magna. Aenean sed pharetra ante, non pulvinar arcu. Nunc massa turpis, volutpat eget euismod a, maximus non justo. Nunc et velit eget sapien vulputate aliquet. Quisque sollicitudin auctor libero, eu feugiat tellus blandit ut. Curabitur iaculis imperdiet mauris.</p>
  </div>
  <a class="abs learn">Learn More &gt;</a>
</section>

<section class="workflow">
  <h2 class="abs sec-title" style="left:225px;top:1272px">Our Work Flow</h2>
  <p class="abs sec-lead" style="top:1271px">Far far away, behind the word mountains, far from the countries Vokalia and Consonantia, there live the blind texts. Separated they live in.</p>

  <div class="flow-step" style="left:225px">
    <div class="flow-circle"><svg width="26" height="26" viewBox="0 0 26 26" fill="none" stroke="#fff" stroke-width="1.4"><path d="M6 22V13c0-4 3-7 7-7s7 3 7 7v9"/><path d="M9 11h8M9 15h8"/></svg></div>
    <div class="flow-line"></div>
    <h3 class="step-title">PERFECTLY DESIGN</h3>
    <p class="step-text">Even the all-powerful Pointing has no control about the blind texts it is an almost unorthographic.</p>
  </div>
  <div class="flow-step" style="left:481px">
    <div class="flow-circle"><svg width="26" height="26" viewBox="0 0 26 26" fill="none" stroke="#fff" stroke-width="1.4"><circle cx="13" cy="7" r="3"/><path d="M11 10L5 23M15 10l6 13M8 17h10"/></svg></div>
    <div class="flow-line"></div>
    <h3 class="step-title">CAREFULLY PLANNED</h3>
    <p class="step-text">Even the all-powerful Pointing has no control about the blind texts it is an almost unorthographic.</p>
  </div>
  <div class="flow-step" style="left:736px">
    <div class="flow-circle"><svg width="26" height="26" viewBox="0 0 26 26" fill="none" stroke="#fff" stroke-width="1.4"><path d="M13 4l9 5-9 5-9-5z"/><path d="M4 13l9 5 9-5M4 17l9 5 9-5"/></svg></div>
    <div class="flow-line"></div>
    <h3 class="step-title">SMARTLY EXECUTE</h3>
    <p class="step-text">Even the all-powerful Pointing has no control about the blind texts it is an almost unorthographic.</p>
  </div>
</section>

<section class="services">
  <h2 class="abs sec-title" style="left:225px;top:1588px">Our Services</h2>
  <p class="abs" style="left:225px;top:1628px;width:240px;font-size:9px;line-height:17px;color:var(--muted)">Even the all-powerful Pointing has no control about the blind texts it is an almost unorthographic.</p>

  <div class="service-card" style="left:481px;top:1588px">
    <svg width="28" height="26" viewBox="0 0 28 26" fill="none" stroke="var(--icon-stroke)" stroke-width="1.2"><path d="M14 2l11 6-11 6-11-6z"/><path d="M3 12l11 6 11-6M3 16l11 6 11-6"/></svg>
    <h3>DESIGN</h3><p>Even the all-powerful Pointing has no control about the blind texts it is an almost unorthographic.</p>
  </div>
  <div class="service-card" style="left:736px;top:1588px">
    <svg width="28" height="26" viewBox="0 0 28 26" fill="none" stroke="var(--icon-stroke)" stroke-width="1.2"><path d="M14 2l11 6-11 6-11-6z"/><path d="M3 12l11 6 11-6M3 16l11 6 11-6"/></svg>
    <h3>INDUSTRIAL DESIGN</h3><p>Even the all-powerful Pointing has no control about the blind texts it is an almost unorthographic.</p>
  </div>
  <div class="service-card" style="left:481px;top:1761px">
    <svg width="28" height="26" viewBox="0 0 28 26" fill="none" stroke="var(--icon-stroke)" stroke-width="1.2"><path d="M14 2l11 6-11 6-11-6z"/><path d="M3 12l11 6 11-6M3 16l11 6 11-6"/></svg>
    <h3>ARCHITECTURE SUPPORT</h3><p>Even the all-powerful Pointing has no control about the blind texts it is an almost unorthographic.</p>
  </div>
  <div class="service-card" style="left:736px;top:1761px">
    <svg width="28" height="26" viewBox="0 0 28 26" fill="none" stroke="var(--icon-stroke)" stroke-width="1.2"><path d="M14 2l11 6-11 6-11-6z"/><path d="M3 12l11 6 11-6M3 16l11 6 11-6"/></svg>
    <h3>RENOVATION</h3><p>Even the all-powerful Pointing has no control about the blind texts it is an almost unorthographic.</p>
  </div>
</section>

<section class="projects">
  <div class="abs eyebrow" style="left:225px;top:2081px">PROJECTS</div>
  <h2 class="abs sec-title" style="left:225px;top:2096px">Featured Projects</h2>
  <p class="abs sec-lead" style="top:2076px">Far far away, behind the word mountains, far from the countries Vokalia and Consonantia, there live the blind texts. Separated they live in. A small river named Duden flows by their place and supplies it with the necessary regelialia. It is a paradisematic country, in which roasted parts of sentences fly into your mouth.</p>
  <div class="abs filters"><b>ALL WORK</b><span>INTERIOR</span><span>EXTERIOR</span><span>LANDSCAPE</span></div>

  <div class="tile" style="left:0;top:2230px;background:linear-gradient(160deg,#f0efec,#e4e2dd)" role="img" aria-label="Wall planter with hanging ivy"></div>
  <div class="tile" style="left:300px;top:2230px;background:linear-gradient(180deg,#eeeef0,#dcdcdf)" role="img" aria-label="Dining room with black table and pendant lamps"></div>
  <div class="tile" style="left:600px;top:2230px;background:linear-gradient(180deg,#f4f3f1 60%,#c3a88a)" role="img" aria-label="White chair and woven basket on wooden floor"></div>
  <div class="tile" style="left:900px;top:2230px;background:linear-gradient(135deg,#e8eef3,#5a9bd6)" role="img" aria-label="White and blue Mediterranean houses"></div>
  <div class="tile" style="left:0;top:2529px;background:linear-gradient(180deg,#e9eaed,#c9cbd0)" role="img" aria-label="Dark skyscraper seen from below"></div>
  <div class="tile" style="left:300px;top:2529px;background:linear-gradient(180deg,#8ab1df,#a7c3e6)" role="img" aria-label="White curved building against blue sky"></div>
  <div class="tile" style="left:600px;top:2529px;background:linear-gradient(90deg,#5a5550,#9e948b 60%,#b7aea5)" role="img" aria-label="Bedside table with alarm clock and plant"></div>
  <div class="tile tile-feature" style="left:900px;top:2529px">
    <div class="kicker">INTERIOR DESIGN</div>
    <h4>Office Interior Design</h4>
    <span class="expand"></span>
  </div>
</section>

<section class="blog">
  <div class="abs blog-band"></div>
  <div class="abs eyebrow" style="left:225px;top:3068px">BLOG</div>
  <h2 class="abs sec-title" style="left:225px;top:3084px">Recent Blog</h2>
  <p class="abs sec-lead" style="top:3066px">Far far away, behind the word mountains, far from the countries Vokalia and Consonantia, there live the blind texts.</p>

  <article class="post" style="left:225px">
    <div class="photo" style="background:linear-gradient(180deg,#8c8a84,#c7bdb3)" role="img" aria-label="Bathroom with freestanding tub and plant"></div>
    <h4>Even the all-powerful Pointing has no control about the blind texts</h4>
  </article>
  <article class="post" style="left:481px">
    <div class="photo" style="background:linear-gradient(180deg,#4c5256,#a9acae)" role="img" aria-label="Modern office corridor with dark walls"></div>
    <h4>Even the all-powerful Pointing has no control about the blind texts</h4>
  </article>
  <article class="post" style="left:736px">
    <div class="photo" style="background:linear-gradient(90deg,#a8856a,#efe9e3 50%,#b88f6d)" role="img" aria-label="Bright room with wooden shelving"></div>
    <h4>Even the all-powerful Pointing has no control about the blind texts</h4>
  </article>
</section>

<section class="clients">
  <div class="abs eyebrow" style="left:225px;top:3563px">CLIENTS</div>
  <h2 class="abs sec-title" style="left:225px;top:3578px">Our CLients</h2>
  <p class="abs sec-lead" style="top:3561px">Far far away, behind the word mountains, far from the countries Vokalia and Consonantia, there live the blind texts.</p>
  <div class="client" style="left:225px">CLIENT LOGO 6</div>
  <div class="client" style="left:379px">CLIENT LOGO 7</div>
  <div class="client" style="left:533px">CLIENT LOGO 1</div>
  <div class="client" style="left:687px">CLIENT LOGO 2</div>
  <div class="client" style="left:840px">CLIENT LOGO 3</div>
  <div class="abs client-dots"><i></i><i></i><i></i><i></i><i></i><i></i><i></i></div>
</section>

<footer class="abs footer">
  <div class="f-col" style="left:225px">
    <h5>Lumaform</h5>
    <p>Far far away, behind the word mountains, far from the countries Vokalia and Consonantia, there live the blind texts.</p>
    <div class="socials">
      <span class="social-dot" role="img" aria-label="Social link"></span>
      <span class="social-dot" role="img" aria-label="Social link"></span>
      <span class="social-dot" role="img" aria-label="Social link"></span>
    </div>
  </div>
  <div class="f-col" style="left:481px">
    <h5>Services</h5>
    <ul class="f-list">
      <li>Architectural Design</li><li>Interior Design</li><li>Exterior Design</li><li>Lighting Design</li><li>CAD Drafting Service</li>
    </ul>
  </div>
  <div class="f-col" style="left:736px;width:238px">
    <h5>Newsletter</h5>
    <p>Far far away, behind the word mountains, far from the countries.</p>
    <div class="field">Enter email address</div>
    <div class="subscribe">Subscribe</div>
  </div>
  <div class="copy">Copyright ©2020 All rights reserved | This template is made by Lumaform Studio</div>
</footer>

</body>
</html>
```